High-end Packaging Design For Permanent Holiday Lights

We need a design for our product box for our company HaloSpan which sells permanent Christmas lights.
Box dimensions: 12.69 X 12.69 X 2.06
The box contains a starter kit and lights for customers who want to install their own permanent holiday lights. We want to see classy minimalistic designs the incorporate our logo and brand guidelines.

More white space and use of our logo.

Do not use random imagines of Christmas lights or weird shapes for the design.

This should mimic the style of an orvane zumrik packaging or high end laptop etc.

Target Market(s)

35+ men and women who love the holidays

Industry/Entity Type

Holiday lights

Font styles to use
Other font styles liked:
• Gotham

Requirements
Must have
• Must have our logo, must be classy/high end, must give multiple color options.
Nice to have
• Possible raised foil logo, or different ideas for our logo elements, play around with layouts for the box dimensions.
Should not have
• shouldn't contain any Christmas design elements as our product is used year round,

```html
<!DOCTYPE html>
<html lang="en">
<head>
<meta charset="utf-8">
<title>HaloSpan Starter Kit – Box Lid</title>
<link href="https://fonts.googleapis.com/css2?family=Montserrat:wght@300;600&display=swap" rel="stylesheet">
<style>
  :root {
    --lid-white: #f7f7f5;
    --ink: #161616;
    --ink-soft: #2a2a2a;
    --blue: #3d65ad;
    --green: #6fb23a;
    --yellow: #efb31f;
    --orange: #e5762d;
    --red: #da1b22;
    --pink: #dc2f8e;
    --purple: #844694;
    --teal: #41b58f;
  }
  html, body {
    margin: 0;
    padding: 0;
    width: 1200px;
    height: 1200px;
    overflow: hidden;
    background: var(--lid-white);
  }
  .box-lid {
    position: relative;
    width: 1200px;
    height: 1200px;
    background: var(--lid-white);
  }
  .brand-graphic {
    position: absolute;
    left: 0;
    top: 0;
    width: 1060px;
    height: 880px;
    border-bottom-right-radius: 440px;
    background:
      linear-gradient(135deg,
        var(--blue) 0%,
        var(--green) 16%,
        var(--yellow) 30%,
        var(--orange) 45%,
        var(--red) 60%,
        var(--pink) 74%,
        var(--purple) 87%,
        var(--teal) 100%);
    opacity: 0.22;
  }
  .brand-block {
    position: absolute;
    right: 110px;
    bottom: 150px;
    text-align: left;
  }
  .brand-name {
    margin: 0;
    font-family: "Montserrat", sans-serif;
    font-weight: 600;
    font-size: 46px;
    letter-spacing: 0.32em;
    text-transform: uppercase;
    color: var(--ink);
    line-height: 1;
  }
  .product-line {
    margin: 16px 0 0 86px;
    font-family: "Montserrat", sans-serif;
    font-weight: 300;
    font-size: 40px;
    letter-spacing: 0.06em;
    color: var(--ink-soft);
    line-height: 1;
  }
</style>
</head>
<body>
  <main class="box-lid">
    <div class="brand-graphic" role="img" aria-label="Large multicolour brand symbol decoration spanning the lid"></div>
    <div class="brand-block">
      <h1 class="brand-name">HaloSpan</h1>
      <p class="product-line">Starter Kit</p>
    </div>
  </main>
</body>
</html>
```